BrightKeel Business Card Contest

We are looking for a modern business card that catches attention and is unique. Attached is the brand guide and logo files. Please note that the back side (not the side with our name and info) with be UV raise printed, so have fun with the design there. We want to include Name, Title, Phone number, email, website.

Contact Information for Business Card

Please see project description

```html
<!DOCTYPE html>
<html lang="en">
<head>
<meta charset="utf-8">
<title>BrightKeel Business Card</title>
<link rel="stylesheet" href="https://fonts.googleapis.com/css2?family=Arimo:wght@400;500;700&display=swap">
<style>
  :root {
    --backdrop: #2e2e30;
    --card-dark: #1f2023;
    --accent-red: #d8321f;
    --accent-orange: #e8801e;
    --accent-blue: #1f7fd0;
    --sky: #27b6e6;
    --mist: #cfd8e0;
    --ink: #17181a;
    --paper: #ffffff;
    --rule: #2aa7d8;
  }
  * { box-sizing: border-box; margin: 0; padding: 0; }
  html, body { width: 1200px; height: 900px; overflow: hidden; }
  body {
    background: var(--backdrop);
    font-family: "Arimo", Arial, sans-serif;
    position: relative;
  }
  .card {
    position: absolute;
    left: 300px;
    width: 600px;
    height: 343px;
    overflow: hidden;
    box-shadow: 0 14px 30px rgba(0,0,0,0.45);
  }
  .card--front {
    top: 70px;
    border-radius: 34px 0 34px 0;
  }
  .card--back {
    top: 487px;
    border-radius: 0 34px 0 34px;
    background: var(--card-dark);
  }
  .front-field {
    position: absolute;
    inset: 0;
    background: linear-gradient(20deg, var(--accent-red) 0%, var(--accent-orange) 22%, var(--mist) 48%, var(--sky) 72%, var(--accent-blue) 100%);
  }
  .front-brand {
    position: absolute;
    inset: 0;
    display: flex;
    align-items: center;
    justify-content: center;
    font-size: 76px;
    font-weight: 500;
    color: var(--ink);
    letter-spacing: 1px;
  }
  .back-shapes { position: absolute; inset: 0; }
  .contact {
    position: absolute;
    left: 40px;
    top: 50px;
    color: var(--paper);
  }
  .contact__name {
    color: var(--accent-red);
    font-weight: 700;
    font-size: 20px;
    letter-spacing: 0.5px;
  }
  .contact__title { font-size: 17px; margin-top: 4px; }
  .contact__rule {
    width: 70px;
    height: 1px;
    background: var(--rule);
    margin: 18px 0 16px;
  }
  .contact__list { list-style: none; font-size: 17px; }
  .contact__list li {
    display: flex;
    align-items: center;
    gap: 10px;
    margin-bottom: 9px;
  }
  .contact__list svg { width: 16px; height: 16px; flex: none; }
  .back-brand {
    position: absolute;
    right: 40px;
    top: 140px;
    display: flex;
    align-items: center;
    gap: 12px;
    color: var(--paper);
    font-size: 50px;
    font-weight: 500;
  }
  .back-brand__mark {
    width: 20px;
    height: 20px;
    background: var(--accent-orange);
  }
</style>
</head>
<body>
  <section class="card card--front">
    <div class="front-field" role="img" aria-label="Triangle mosaic pattern fading from orange through pale grey to bright blue"></div>
    <div class="front-brand">BrightKeel</div>
  </section>

  <section class="card card--back">
    <svg class="back-shapes" viewBox="0 0 600 343" preserveAspectRatio="none" aria-hidden="true">
      <polygon points="90,120 460,120 360,260 0,260" fill="#4a2320" opacity="0.75"/>
      <polygon points="0,200 440,200 600,343 0,343" fill="#2f3338"/>
      <polygon points="0,270 600,300 600,343 0,343" fill="#1d3a44" opacity="0.8"/>
    </svg>
    <div class="contact">
      <p class="contact__name">DANA WHITLOW</p>
      <p class="contact__title">Director</p>
      <div class="contact__rule"></div>
      <ul class="contact__list">
        <li>
          <svg viewBox="0 0 16 16"><path d="M3 1.5l3 .5 1 3-2 1.5a9 9 0 0 0 4.5 4.5L11 9l3 1 .5 3-2 1.5C7 14 2 9 1.5 3.5z" fill="var(--accent-orange)"/></svg>
          300-410-7720
        </li>
        <li>
          <svg viewBox="0 0 16 16"><rect x="1" y="3" width="14" height="10" fill="var(--accent-orange)"/><path d="M1 3l7 6 7-6" stroke="var(--card-dark)" stroke-width="1.3" fill="none"/></svg>
          info@BrightKeel.com
        </li>
        <li>
          <svg viewBox="0 0 16 16" fill="none" stroke="var(--accent-orange)" stroke-width="1.3"><circle cx="8" cy="8" r="6.5"/><ellipse cx="8" cy="8" rx="3" ry="6.5"/><path d="M1.5 8h13M2.5 5h11M2.5 11h11"/></svg>
          www.BrightKeel.com
        </li>
      </ul>
    </div>
    <div class="back-brand">
      <span class="back-brand__mark"></span>
      <span>BrightKeel</span>
    </div>
  </section>
</body>
</html>
```